Mobile (Android/iPhone) game studio needs stationary design and a business card

We are Plunk Ferret Software and we need a fun and creative stationary design. Our company builds Android and iPhone games and children's software. The stationary designs should reflect an entertainment, fun and creativity. The pieces of stationary we need are:
1. A4 and Letter Word template (company letterhead)
2. A4 and Letter PPT template
3. Business card
4. Envelopes of various standard sizes
Each of the designs should somehow utilize our company logo.
The business card should have the following:
1. Incorporates our company logo (see attached)
2. Has a front and back with the same design (front is English, back is Traditional Chinese)
3. Delivered in an editable template so we can easily add new business cards using the same template when we hire more employees
4. Field for full name
5. Field for employee's title
6. Field for employee's email address
7. Field for company phone number - +886-2-51384470
8. Field for mobile phone number
9. Field for company fax number - +886-2-51384492
10. Company website address: www.plunkferret.example
11. Company address (on English side): 7F-2, NO. 63, Lane 91, Guoyuan Road, Dali District, Taipei Taiwan
12. Company address (on Traditional Chinese side): See Word document attachment for address in Chinese characters
Industry/Entity Type
Games
Look and feel
Each slider illustrates characteristics of the customer's brand and the style your logo design should communicate.

```html
<!DOCTYPE html>
<html lang="en">
<head>
<meta charset="utf-8">
<title>Plunk Ferret Software – Stationery</title>
<link rel="stylesheet" href="https://fonts.googleapis.com/css2?family=Didact+Gothic&family=Noto+Sans+TC:wght@400&display=swap">
<style>
  :root {
    --backdrop: #161616;
    --paper: #eef0f3;
    --navy: #16155e;
    --indigo: #2b2a8c;
    --brand-blue: #1e88d6;
    --card-blue-dark: #0c3f8a;
    --card-blue: #1559b0;
    --ink: #555a66;
    --ink-soft: #8a8f99;
    --swoosh-grey: #8c8c8c;
    --white: #ffffff;
    --text: "Didact Gothic", Arial, sans-serif;
    --text-tc: "Noto Sans TC", sans-serif;
  }
  * { box-sizing: border-box; margin: 0; padding: 0; }
  html, body { width: 1200px; height: 900px; overflow: hidden; }
  body { background: var(--backdrop); font-family: var(--text); position: relative; }

  .swoosh { position: absolute; left: 0; width: 100%; display: block; }

  .brand { display: flex; align-items: center; gap: 6px; }
  .brand-dot { width: 14px; height: 14px; border-radius: 50%; background: var(--brand-blue); flex: none; }
  .brand-name { font-family: var(--text); font-size: 14px; color: var(--brand-blue); white-space: nowrap; }

  /* Letterhead */
  .letterhead {
    position: absolute; left: 40px; top: 54px; width: 560px; height: 792px;
    background: var(--paper);
  }
  .letterhead .swoosh-top { top: 20px; }
  .letterhead .masthead { position: absolute; left: 216px; top: 33px; }
  .letterhead .contact { margin-top: 6px; font-size: 7px; color: var(--ink-soft); line-height: 1.6; }
  .letterhead .swoosh-bottom { bottom: 26px; }
  .letterhead .site { position: absolute; bottom: 14px; width: 100%; text-align: center; font-size: 9px; color: var(--ink-soft); }

  /* Business cards */
  .card { position: absolute; left: 640px; width: 350px; height: 200px; overflow: hidden; }
  .card-front {
    top: 54px;
    background:
      repeating-linear-gradient(120deg, rgba(255,255,255,0.04) 0 10px, rgba(255,255,255,0) 10px 22px),
      linear-gradient(160deg, var(--card-blue) 0%, var(--card-blue-dark) 100%);
    color: var(--white);
  }
  .card-front .brand-name { color: var(--white); }
  .card-front .brand-dot { background: var(--white); }
  .card-back { top: 262px; background: var(--paper); color: var(--ink); }
  .card .card-body { position: absolute; left: 28px; top: 52px; }
  .card-back .card-body { top: 44px; }
  .card .full-name { font-size: 11px; letter-spacing: 1px; margin-top: 10px; }
  .card-back .full-name { color: var(--navy); }
  .card .details { font-size: 6.5px; line-height: 1.6; }
  .card-back .details .label { color: var(--brand-blue); }
  .card .address-tc { font-family: var(--text-tc); font-size: 6.5px; letter-spacing: 1px; }
  .card .site { position: absolute; bottom: 8px; width: 100%; text-align: center; font-size: 6.5px; }
  .card-front .site { color: #d6def0; }
  .card-back .site { color: var(--ink-soft); }
  .card-front .illustration-area {
    position: absolute; right: 0; top: 0; width: 150px; height: 70px;
    background: linear-gradient(200deg, rgba(214,226,242,0.35) 0%, rgba(21,89,176,0) 85%);
  }
  .card-back .swoosh-top { top: 0; }
  .card .swoosh-bottom { bottom: 18px; }

  /* Envelope */
  .envelope {
    position: absolute; left: 620px; top: 500px; width: 560px; height: 300px;
    background: var(--paper);
  }
  .envelope .flap {
    position: absolute; left: 0; top: -30px; width: 100%; height: 62px;
    background: linear-gradient(180deg, #1f64c4 0%, #0d4599 100%);
    border-radius: 40px 40px 0 0;
  }
  .envelope .swoosh-top { top: 24px; }
  .envelope .masthead { position: absolute; left: 226px; top: 36px; }
  .envelope .contact { position: absolute; left: 226px; top: 76px; font-size: 10px; color: var(--ink); line-height: 1.9; }
  .envelope .contact .label { color: var(--brand-blue); }
  .envelope .window {
    position: absolute; right: 18px; bottom: 40px; width: 300px; height: 66px;
    background: var(--white); border-radius: 12px;
  }
</style>
</head>
<body>

<section class="letterhead">
  <svg class="swoosh swoosh-top" viewBox="0 0 560 40" height="40" aria-hidden="true">
    <path d="M0,4 Q120,22 206,20 L206,24 Q120,28 0,12 Z" fill="var(--navy)"/>
    <path d="M560,4 Q460,22 376,20 L376,24 Q460,28 560,12 Z" fill="var(--indigo)"/>
  </svg>
  <div class="masthead">
    <div class="brand"><span class="brand-dot"></span><span class="brand-name">Plunk Ferret Software</span></div>
    <div class="contact">P+886-2-51384470 | F+886-2-51384492<br>7F-2, NO. 63, Lane 91, Guoyuan Road, Dali District, Taipei Taiwan</div>
  </div>
  <svg class="swoosh swoosh-bottom" viewBox="0 0 560 20" height="20" aria-hidden="true">
    <path d="M0,18 Q120,4 220,6 L220,9 Q120,8 0,20 Z" fill="var(--swoosh-grey)"/>
    <path d="M560,18 Q440,4 340,6 L340,9 Q440,8 560,20 Z" fill="var(--swoosh-grey)"/>
  </svg>
  <div class="site">www.plunkferret.example</div>
</section>

<section class="card card-front">
  <div class="illustration-area" role="img" aria-label="Area for the playful brand illustration in white and blue tones"></div>
  <div class="card-body">
    <div class="brand"><span class="brand-dot"></span><span class="brand-name">Plunk Ferret Software</span></div>
    <div class="full-name">Full Name</div>
    <div class="details">Occupation | name@plunkferret.example<br>P+886-2-51384470 | M+886-2-51384470 | F+886-2-51384492</div>
    <div class="address-tc" lang="zh-Hant">台灣台北市大里區國原路91巷63號7樓之2</div>
  </div>
  <svg class="swoosh swoosh-bottom" viewBox="0 0 350 14" height="14" aria-hidden="true">
    <path d="M0,2 Q175,12 350,2 L350,5 Q175,14 0,5 Z" fill="var(--swoosh-grey)"/>
  </svg>
  <div class="site">www.plunkferret.example</div>
</section>

<section class="card card-back">
  <svg class="swoosh swoosh-top" viewBox="0 0 350 14" height="14" aria-hidden="true">
    <path d="M0,2 Q175,12 350,2 L350,5 Q175,14 0,5 Z" fill="var(--navy)"/>
  </svg>
  <div class="card-body">
    <div class="brand"><span class="brand-dot"></span><span class="brand-name">Plunk Ferret Software</span></div>
    <div class="full-name">Full Name</div>
    <div class="details"><span class="label">Occupation</span> | name@plunkferret.example<br>P+886-2-51384470 | M+886-2-51384470 | F+886-2-51384492<br>7F-2, NO. 63, Lane 91, Guoyuan Road, Dali District, Taipei Taiwan</div>
  </div>
  <svg class="swoosh swoosh-bottom" viewBox="0 0 350 10" height="10" aria-hidden="true">
    <path d="M0,9 Q60,2 120,3 L120,5 Q60,5 0,10 Z" fill="var(--navy)"/>
    <path d="M350,9 Q290,2 230,3 L230,5 Q290,5 350,10 Z" fill="var(--indigo)"/>
  </svg>
  <div class="site">www.plunkferret.example</div>
</section>

<section class="envelope">
  <div class="flap"></div>
  <svg class="swoosh swoosh-top" viewBox="0 0 560 30" height="30" aria-hidden="true">
    <path d="M0,2 Q130,16 216,18 L216,22 Q130,22 0,7 Z" fill="var(--navy)"/>
    <path d="M560,2 Q460,16 388,18 L388,22 Q460,22 560,7 Z" fill="var(--indigo)"/>
  </svg>
  <div class="masthead">
    <div class="brand"><span class="brand-dot"></span><span class="brand-name">Plunk Ferret Software</span></div>
  </div>
  <div class="contact">
    <span class="label">P</span>+886-2-51384470 | <span class="label">F</span>+886-2-51384492<br>
    7F-2, NO. 63, Lane 91, Guoyuan Road, Dali District, Taipei Taiwan
  </div>
  <div class="window"></div>
</section>

</body>
</html>
```